Cedar Hollow Morning Light Minister

Need this banner to stand out, and look like a poster for a movie. The Color scheme, I'm looking for are darker, more dismal doom and gloom? and make it say be heal and be delivered TODAY.

```html
<!DOCTYPE html>
<html lang="en">
<head>
<meta charset="UTF-8">
<title>Be Healed and Be Delivered Today – Street Banner</title>
<link href="https://fonts.googleapis.com/css2?family=Oswald:wght@300;400;500;600;700&display=swap" rel="stylesheet">
<style>
  :root {
    --page-bg: #ffffff;
    --ink-white: #ffffff;
    --ink-orange: #f6a46c;
    --night: #1a0b16;
    --plum: #3d1428;
    --crimson: #8c1838;
    --smoke: #b78a9c;
    --circle-core: #c2143f;
    --circle-edge: #7a1233;
  }
  * { margin: 0; padding: 0; box-sizing: border-box; }
  html, body {
    width: 1200px;
    height: 1200px;
    overflow: hidden;
    background: var(--page-bg);
  }
  .stage {
    position: relative;
    width: 1200px;
    height: 1200px;
  }
  .banner {
    position: absolute;
    left: 455px;
    top: 75px;
    width: 290px;
    height: 1050px;
    overflow: hidden;
    box-shadow: -30px 0 60px rgba(0,0,0,0.18);
    font-family: "Oswald", sans-serif;
    color: var(--ink-white);
    text-align: center;
  }
  .banner__backdrop {
    position: absolute;
    inset: 0;
    width: 100%;
    height: 100%;
  }
  .line {
    position: absolute;
    left: 0;
    width: 100%;
    line-height: 1;
    white-space: nowrap;
    text-transform: uppercase;
  }
  .line__fit {
    display: inline-block;
    transform-origin: center top;
  }
  .headline-got {
    top: 57px;
    font-size: 168px;
    font-weight: 700;
    letter-spacing: -4px;
  }
  .headline-got .line__fit { transform: scaleX(0.9); }
  .headline-demons {
    top: 215px;
    font-size: 68px;
    font-weight: 600;
    letter-spacing: -1px;
    color: var(--ink-orange);
  }
  .headline-demons .line__fit { transform: scaleX(0.93); }
  .minister-name {
    position: absolute;
    top: 326px;
    left: 0;
    width: 100%;
    font-size: 40px;
    line-height: 42px;
    letter-spacing: -0.5px;
  }
  .minister-name__light { font-weight: 400; display: block; }
  .minister-name__bold { font-weight: 700; display: block; }
  .cta {
    font-weight: 600;
    letter-spacing: -2px;
  }
  .cta-heal { top: 568px; font-size: 86px; }
  .cta-and { top: 643px; font-size: 86px; }
  .cta-heal .line__fit,
  .cta-and .line__fit { transform: scaleX(0.86); }
  .cta-delivered {
    top: 728px;
    font-size: 66px;
    color: var(--ink-orange);
    letter-spacing: -1.5px;
  }
  .cta-delivered .line__fit { transform: scaleX(0.88); }
  .cta-today {
    top: 780px;
    font-size: 104px;
    color: var(--ink-orange);
    letter-spacing: -3px;
  }
  .cta-today .line__fit { transform: scaleX(0.87); }
  .web-address {
    position: absolute;
    left: 0;
    width: 100%;
    top: 958px;
    font-size: 24px;
    font-weight: 400;
    letter-spacing: 0.5px;
  }
</style>
</head>
<body>
<div class="stage">
  <section class="banner">
    <svg class="banner__backdrop" viewBox="0 0 290 1050" preserveAspectRatio="none" role="img" aria-label="Dark smoky red storm clouds">
      <defs>
        <linearGradient id="skyFade" x1="0" y1="0" x2="0" y2="1">
          <stop offset="0" stop-color="#1a0b16"/>
          <stop offset="0.22" stop-color="#5a1a32"/>
          <stop offset="0.45" stop-color="#4a1a33"/>
          <stop offset="0.75" stop-color="#3b1327"/>
          <stop offset="1" stop-color="#1e0b17"/>
        </linearGradient>
        <radialGradient id="smokeGlow" cx="0.85" cy="0.45" r="0.4">
          <stop offset="0" stop-color="#b78a9c" stop-opacity="0.85"/>
          <stop offset="1" stop-color="#b78a9c" stop-opacity="0"/>
        </radialGradient>
        <radialGradient id="redCircle" cx="0.55" cy="0.45" r="0.6">
          <stop offset="0" stop-color="#c2143f"/>
          <stop offset="0.7" stop-color="#9e1538"/>
          <stop offset="1" stop-color="#7a1233"/>
        </radialGradient>
      </defs>
      <rect width="290" height="1050" fill="url(#skyFade)"/>
      <rect width="290" height="1050" fill="url(#smokeGlow)"/>
      <circle cx="145" cy="727" r="210" fill="url(#redCircle)" opacity="0.9"/>
    </svg>

    <div class="line headline-got"><span class="line__fit">Got</span></div>
    <div class="line headline-demons"><span class="line__fit">Demons?</span></div>

    <div class="minister-name">
      <span class="minister-name__light">Cedar Hollow</span>
      <span class="minister-name__light">Morning</span>
      <span class="minister-name__bold">Light</span>
      <span class="minister-name__bold">Minister</span>
    </div>

    <div class="line cta cta-heal"><span class="line__fit">Be Heal</span></div>
    <div class="line cta cta-and"><span class="line__fit">And Be</span></div>
    <div class="line cta cta-delivered"><span class="line__fit">Delivered</span></div>
    <div class="line cta cta-today"><span class="line__fit">Today</span></div>

    <div class="web-address">morninglightministries.com</div>
  </section>
</div>
</body>
</html>
```